Clinical Layout Builders - Stationery
Biz Cards + Stationary
Clinical Layout Builders - Stationery - Information Technology
Creative Brief
Professional
Dr. Elena M. Castillo
Director of Content Development
Ceiba Business Plaza #3, Suite 118 San Juan, PR 00941
(787) PENDING
elena.castillo@hnvwqbt.com
www.hnvwqbt.com
Need a second set of cards for: Dr. Luis F. Beltran Business Development Director Same info- address, fax and phone (Pending) Cell: (787) 555-0192 Email: luis.beltran@hnvwqbt.com
Either the logo, the website or something else. Feel free to be creative!

```html
<!DOCTYPE html>
<html lang="en">
<head>
<meta charset="utf-8">
<title>Clinical Layout Builders – Business Cards</title>
<link href="https://fonts.googleapis.com/css2?family=Montserrat:wght@400;600;700&display=swap" rel="stylesheet">
<style>
  :root {
    --backdrop: #ecebe8;
    --magenta: #a3206f;
    --magenta-light: #c23a8e;
    --magenta-dark: #7a1453;
    --card-black: #111114;
    --card-black-soft: #25252a;
    --ink-light: #f2f2f2;
    --ink-muted: #bdbdc2;
  }
  * { box-sizing: border-box; margin: 0; padding: 0; }
  html, body {
    width: 1200px; height: 1088px; overflow: hidden;
    background: var(--backdrop);
    font-family: "Montserrat", Arial, sans-serif;
  }
  .stage { position: relative; width: 1200px; height: 1088px; }

  /* Front card */
  .card-front {
    position: absolute; left: 300px; top: 210px;
    width: 690px; height: 420px; border-radius: 22px; overflow: hidden;
    background: radial-gradient(ellipse at 55% 35%, var(--card-black-soft), var(--card-black) 70%);
    box-shadow: 0 14px 30px rgba(0,0,0,.35);
  }
  .card-front__strip {
    position: absolute; left: 0; top: 0; bottom: 0; width: 105px;
    background: linear-gradient(90deg, var(--magenta-dark), var(--magenta) 60%, var(--magenta-light));
  }
  .card-front__web {
    position: absolute; left: 52px; top: 210px;
    transform: translate(-50%, -50%) rotate(90deg);
    color: var(--ink-light); font-size: 17px; letter-spacing: 1px; white-space: nowrap;
  }
  .card-front__brand {
    position: absolute; left: 105px; right: 0; top: 90px;
    text-align: center; color: var(--magenta-light);
    font-size: 34px; font-weight: 700; letter-spacing: 1px;
  }
  .card-front__person { position: absolute; left: 135px; top: 235px; color: var(--ink-light); }
  .person-name { font-size: 21px; font-weight: 400; }
  .person-title { font-size: 13px; color: var(--ink-muted); margin-top: 6px; }
  .card-front__contact {
    position: absolute; left: 450px; top: 225px; color: var(--ink-light);
    font-size: 13px; line-height: 1.5;
  }
  .contact-address { margin-bottom: 12px; }
  .contact-line { display: flex; align-items: center; gap: 9px; margin-bottom: 3px; }
  .contact-line svg { width: 14px; height: 14px; flex: none; fill: var(--ink-light); }

  /* Back card */
  .card-back {
    position: absolute; left: 330px; top: 580px;
    width: 660px; height: 290px; border-radius: 22px; overflow: hidden;
    background: radial-gradient(ellipse at 50% 45%, var(--magenta-light), var(--magenta) 55%, var(--magenta-dark));
    box-shadow: 0 14px 30px rgba(0,0,0,.35);
  }
  .card-back__brand {
    position: absolute; left: 0; right: 0; top: 120px; text-align: center;
    color: var(--ink-light); font-size: 40px; font-weight: 700; letter-spacing: 1px;
  }
</style>
</head>
<body>
<main class="stage">
  <section class="card-front" aria-label="Business card front">
    <div class="card-front__strip"></div>
    <div class="card-front__web">www.hnvwqbt.com</div>
    <div class="card-front__brand">Clinical Layout Builders</div>
    <div class="card-front__person">
      <p class="person-name">Dr. Elena M. Castillo</p>
      <p class="person-title">Director of Content Development</p>
    </div>
    <div class="card-front__contact">
      <p class="contact-address">Ceiba Business Plaza #3, Suite 118<br>San Juan, PR 00941</p>
      <p class="contact-line">
        <svg viewBox="0 0 16 16"><path d="M3 1h3l1.5 4-2 1.3a9 9 0 0 0 4.2 4.2L11 8.5l4 1.5v3a2 2 0 0 1-2 2A12 12 0 0 1 1 3a2 2 0 0 1 2-2z"/></svg>
        (787) PENDING
      </p>
      <p class="contact-line">
        <svg viewBox="0 0 16 16"><rect x="4" y="0.5" width="8" height="15" rx="1.6"/><rect x="5.5" y="2.5" width="5" height="9" fill="#111114"/></svg>
        (787) 555-0147
      </p>
      <p class="contact-line">
        <svg viewBox="0 0 16 16"><rect x="1" y="6" width="14" height="8" rx="1"/><rect x="4" y="1" width="8" height="5"/></svg>
        (787) 555-0163
      </p>
      <p class="contact-line">
        <svg viewBox="0 0 16 16"><rect x="1" y="3" width="14" height="10" rx="1"/><path d="M1.5 3.5 8 9l6.5-5.5" fill="none" stroke="#111114" stroke-width="1.3"/></svg>
        elena.castillo@hnvwqbt.com
      </p>
    </div>
  </section>

  <section class="card-back" aria-label="Business card back">
    <div class="card-back__brand">Clinical Layout Builders</div>
  </section>
</main>
</body>
</html>
```